Business Card Design for a Design/Build Firm

Harrowgate Structures Group, Inc. is a firm providing construction professional project management and architectural design services to an international clientele. Contemporary. "Green" movement aware. Business card to have back design/logo. Cards will be on high gloss paper

Target Market(s)

Building Developers and Owners

Industry/Entity Type

Construction

Requirements
Nice to have
• We really would like to use the acronym "HSG" as main focal point fo card design. Company will be known as HSG.
Should not have
• No globes or abstract images of buildings.

```html
<!DOCTYPE html>
<html lang="en">
<head>
<meta charset="utf-8">
<title>HSG Business Card — Front and Back</title>
<link rel="stylesheet" href="https://fonts.googleapis.com/css2?family=Source+Sans+3:wght@400;600;700&display=swap">
<style>
  :root {
    --brand-green: #72a135;
    --paper-white: #ffffff;
    --rule-grey: #9a9a9a;
    --text-grey: #7a7a7a;
    --backdrop: #3b3b3b;
    --font-main: "Source Sans 3", "Helvetica Neue", Arial, sans-serif;
  }
  * { margin: 0; padding: 0; box-sizing: border-box; }
  html, body {
    width: 1200px; height: 900px; overflow: hidden;
    background: var(--backdrop);
    font-family: var(--font-main);
  }
  .stage { position: relative; width: 1200px; height: 900px; }

  .card {
    position: absolute; left: 280px;
    width: 640px; height: 366px;
    overflow: hidden;
    box-shadow: 0 6px 18px rgba(0,0,0,0.45);
  }

  /* Back of card */
  .card-back { top: 44px; background: var(--brand-green); }
  .card-back .wordmark {
    position: absolute; right: 44px; bottom: 50px; text-align: right;
    color: var(--paper-white);
  }
  .wordmark-letters {
    font-weight: 400; font-size: 78px; line-height: 0.9; letter-spacing: 1px;
  }
  .wordmark-name { font-size: 17px; font-weight: 400; margin-top: 4px; }

  /* Front of card */
  .card-front { top: 490px; background: var(--paper-white); }
  .card-front .upper { position: absolute; left: 0; top: 0; width: 100%; height: 170px; }
  .card-front .divider-rule {
    position: absolute; left: 0; top: 170px; width: 100%; height: 2px; background: var(--rule-grey);
  }
  .card-front .lower {
    position: absolute; left: 0; top: 178px; width: 100%; height: 188px; background: var(--brand-green);
  }
  .card-front .wordmark {
    position: absolute; left: 40px; top: 26px; color: var(--brand-green);
  }
  .card-front .wordmark-letters { font-size: 70px; }
  .card-front .wordmark-name { font-size: 14px; color: var(--text-grey); margin-top: 2px; }

  .person {
    position: absolute; right: 36px; top: 108px; text-align: right;
  }
  .person-name { color: var(--brand-green); font-weight: 700; font-size: 23px; line-height: 1.05; }
  .person-title { color: var(--text-grey); font-size: 17px; line-height: 1.2; }

  .address {
    position: absolute; left: 40px; top: 22px;
    color: var(--paper-white); font-size: 16px; line-height: 1.3;
  }

  .contacts {
    position: absolute; right: 130px; top: 70px; text-align: right;
    color: var(--paper-white); font-size: 16px; line-height: 24px;
  }
  .contact-divider {
    position: absolute; left: 520px; top: 70px; width: 1px; height: 98px;
    background: rgba(255,255,255,0.7);
  }
  .contact-icons { position: absolute; left: 532px; top: 70px; }
  .contact-icons svg { display: block; width: 16px; height: 24px; }
</style>
</head>
<body>
<main class="stage">

  <section class="card card-back" aria-label="Card back">
    <div class="wordmark">
      <div class="wordmark-letters">HSG</div>
      <div class="wordmark-name">Harrowgate Structures Group, Inc.</div>
    </div>
  </section>

  <section class="card card-front" aria-label="Card front">
    <div class="upper">
      <div class="wordmark">
        <div class="wordmark-letters">HSG</div>
        <div class="wordmark-name">Harrowgate Structures Group, Inc.</div>
      </div>
      <div class="person">
        <div class="person-name">Marcus Hale</div>
        <div class="person-title">Marketing Manager</div>
      </div>
    </div>
    <div class="divider-rule"></div>
    <div class="lower">
      <address class="address" style="font-style:normal">
        1187 Linden Park Road, #214<br>
        Easton, PA 18042
      </address>

      <div class="contacts">
        <div>800-555-0172</div>
        <div>587-555-0318</div>
        <div>marcus@harrowgatesg.com</div>
        <div>www.harrowgatesg.com</div>
      </div>
      <div class="contact-divider"></div>
      <div class="contact-icons">
        <svg viewBox="0 0 16 24" aria-label="Office phone">
          <path d="M2 10 Q8 5 14 10 L12.5 12 L10.5 11 L10.5 10 Q8 9 5.5 10 L5.5 11 L3.5 12 Z" fill="#fff"/>
          <rect x="4" y="13" width="8" height="5" rx="1" fill="#fff"/>
        </svg>
        <svg viewBox="0 0 16 24" aria-label="Mobile phone">
          <rect x="2" y="14" width="2.2" height="4" fill="#fff"/>
          <rect x="5.5" y="12" width="2.2" height="6" fill="#fff"/>
          <rect x="9" y="10" width="2.2" height="8" fill="#fff"/>
          <rect x="12.5" y="8" width="2.2" height="10" fill="#fff"/>
        </svg>
        <svg viewBox="0 0 16 24" aria-label="Email">
          <rect x="1.5" y="8.5" width="13" height="9" fill="none" stroke="#fff" stroke-width="1.2"/>
          <path d="M1.5 8.5 L8 13.5 L14.5 8.5" fill="none" stroke="#fff" stroke-width="1.2"/>
        </svg>
        <svg viewBox="0 0 16 24" aria-label="Website">
          <circle cx="8" cy="13" r="6" fill="none" stroke="#fff" stroke-width="1.2"/>
          <line x1="2" y1="13" x2="14" y2="13" stroke="#fff" stroke-width="1"/>
          <ellipse cx="8" cy="13" rx="2.5" ry="6" fill="none" stroke="#fff" stroke-width="1"/>
        </svg>
      </div>
    </div>
  </section>

</main>
</body>
</html>
```